Flyer Design

I need a flyer to advertise my
home parties for hens night and girls nights
we offer free parties and premium parties from $149
needed to hand out at other parties and in orders.
I have a logo and would like to include a pic or 2
colours mainly black and pinks.
Mainly letting customers know what we offer, packages,
how to book, and an offer for booking now.

Target Market(s)

women 18+

Requirements
Must have
• Details include but words can be changed to suit-
Free home parties, party games and novelties, Velvet Evenings photo booth, And male entertainers
loads of host and hens gifts
games and trivia lots to choose from with
adult toys lingerie costumes corsets
book at www.cherryandlace-example.com
or 0482957164
book today and get a upgrade to premium games prize pack $50 value+

Nice to have
• make me want to book a party, you can be creative.

```html
<!DOCTYPE html>
<html lang="en">
<head>
<meta charset="utf-8">
<title>Fun in the Bedroom Parties – Cherry &amp; Lace</title>
<link rel="stylesheet" href="https://fonts.googleapis.com/css2?family=Cinzel:wght@400&family=Tinos:wght@400;700&display=swap">
<style>
  :root {
    --frame-pink: #e0399a;
    --frame-glow: #b0207a;
    --night: #050205;
    --title-white: #ffffff;
    --copy-yellow: #f3ea5a;
    --rule-gold: #c9b23a;
    --skin-light: #c99a86;
    --skin-shade: #6a3f36;
    --logo-fill: #d9a8c8;
    --logo-ink: #3a1438;
  }
  * { margin: 0; padding: 0; box-sizing: border-box; }
  html, body { width: 1200px; height: 851px; overflow: hidden; background: var(--night); }
  .flyer {
    position: relative;
    width: 1200px;
    height: 851px;
    overflow: hidden;
    background: var(--frame-pink);
  }
  .flyer__stage {
    position: absolute;
    inset: 14px;
    border-radius: 26px;
    background: var(--night);
    box-shadow: 0 0 30px 14px var(--frame-glow), inset 0 0 60px 20px rgba(200,40,140,0.55);
    overflow: hidden;
  }
  .flyer__glow {
    position: absolute;
    left: 300px; top: 170px;
    width: 620px; height: 380px;
    background: radial-gradient(ellipse at center, rgba(160,70,170,0.85) 0%, rgba(110,40,120,0.55) 40%, rgba(5,2,5,0) 75%);
  }
  .photo { position: absolute; opacity: 0.9; }
  .photo--left {
    left: 56px; top: 0; width: 290px; height: 823px;
    background: radial-gradient(ellipse 55% 48% at 45% 45%, var(--skin-light) 0%, var(--skin-shade) 55%, rgba(5,2,5,0) 100%);
  }
  .photo--right {
    left: 598px; top: 0; width: 580px; height: 823px;
    background: radial-gradient(ellipse 45% 50% at 55% 42%, var(--skin-light) 0%, var(--skin-shade) 55%, rgba(5,2,5,0) 100%);
  }
  .streaks { position: absolute; left: 0; top: 0; }
  .streaks line { stroke: rgba(255,255,255,0.18); stroke-width: 1.5; }
  .brand {
    position: absolute;
    left: 539px; top: 51px;
    width: 84px; height: 84px;
    border-radius: 50%;
    background: var(--logo-fill);
    display: flex; align-items: center; justify-content: center;
    text-align: center;
    font-family: 'Tinos', serif;
    font-size: 14px;
    line-height: 1.15;
    color: var(--logo-ink);
  }
  .headline {
    position: absolute;
    left: 0; top: 0;
    font-family: 'Cinzel', serif;
    color: var(--title-white);
    font-weight: 400;
    text-shadow: 0 0 8px rgba(255,255,255,0.35);
  }
  .headline span { position: absolute; white-space: nowrap; line-height: 1; }
  .headline__fun { left: 352px; top: 161px; font-size: 165px; letter-spacing: 3px; }
  .headline__in { left: 725px; top: 162px; font-size: 88px; }
  .headline__the { left: 727px; top: 252px; font-size: 56px; }
  .headline__bedroom { left: 345px; top: 316px; font-size: 84px; letter-spacing: 7px; }
  .headline__parties { left: 345px; top: 390px; font-size: 127px; }
  .rule {
    position: absolute;
    left: 400px; width: 450px; height: 3px;
    background: linear-gradient(90deg, rgba(201,178,58,0) 0%, var(--rule-gold) 30%, var(--rule-gold) 70%, rgba(201,178,58,0) 100%);
  }
  .rule--top { top: 522px; }
  .rule--bottom { top: 768px; }
  .offer {
    position: absolute;
    left: 0; width: 1172px; top: 548px;
    text-align: center;
    font-family: 'Tinos', serif;
    font-size: 24px;
    line-height: 27.5px;
    color: var(--copy-yellow);
  }
  .offer strong { font-weight: 700; }
</style>
</head>
<body>
<div class="flyer">
  <div class="flyer__stage">
    <div class="photo photo--left" role="img" aria-label="Photo of a woman in red lace lingerie"></div>
    <div class="photo photo--right" role="img" aria-label="Photo of a woman in a patterned bikini"></div>
    <div class="flyer__glow"></div>
    <svg class="streaks" width="1172" height="823">
      <line x1="300" y1="180" x2="900" y2="180"/>
      <line x1="280" y1="300" x2="920" y2="300"/>
      <line x1="320" y1="385" x2="880" y2="385"/>
      <line x1="340" y1="448" x2="860" y2="448"/>
    </svg>
    <div class="brand">Cherry<br>&amp;<br>Lace</div>
    <h1 class="headline">
      <span class="headline__fun">FUN</span>
      <span class="headline__in">IN</span>
      <span class="headline__the">THE</span>
      <span class="headline__bedroom">BEDROOM</span>
      <span class="headline__parties">PARTIES</span>
    </h1>
    <div class="rule rule--top"></div>
    <div class="offer">
      <p>Free home parties, party games and novelties, Velvet Evenings photo booth, and male entertainers</p>
      <p>Loads of host and hens gifts</p>
      <p>Games and trivia lots to choose from with</p>
      <p>Adult toys lingerie costumes corsets</p>
      <p>Book at <strong>www.cherryandlace-example.com</strong></p>
      <p>or <strong>0482957164</strong></p>
      <p>+book today and get a upgrade to premium games prize pack <strong>$50 value</strong></p>
    </div>
    <div class="rule rule--bottom"></div>
  </div>
</div>
</body>
</html>
```